Meridian Works Consultancy needs a business card design

Business card should represent civil engineering infrastructure projects such as roads, bridges, tunnels, rail, rail, pipelines, structures and resource infrastructure

Industry/Entity Type

Business

```html
<!DOCTYPE html>
<html lang="en">
<head>
<meta charset="utf-8">
<title>Meridian Works Consultancy – Business Card</title>
<link href="https://fonts.googleapis.com/css2?family=Archivo+Narrow:wght@600;700&display=swap" rel="stylesheet">
<style>
  :root {
    --paper: #ffffff;
    --navy: #020f7a;
    --gold: #c88f1e;
    --brand-blue: #0a2bd6;
    --ink-light: #ffffff;
  }
  * { margin: 0; padding: 0; box-sizing: border-box; }
  html, body {
    width: 1200px;
    height: 675px;
    overflow: hidden;
    background: var(--paper);
  }
  .card {
    position: relative;
    width: 1200px;
    height: 675px;
    background: var(--paper);
    font-family: "Archivo Narrow", "Arial Narrow", sans-serif;
  }
  .brand-mark {
    position: absolute;
    left: 150px;
    top: 90px;
    width: 150px;
    height: 150px;
  }
  .brand-name {
    position: absolute;
    left: 382px;
    top: 78px;
    font-size: 132px;
    font-weight: 700;
    line-height: 1;
    color: var(--brand-blue);
    letter-spacing: 2px;
  }
  .brand-rule {
    position: absolute;
    left: 366px;
    top: 218px;
    width: 320px;
    height: 4px;
    background: var(--gold);
  }
  .gold-band {
    position: absolute;
    left: 0;
    top: 290px;
    width: 1200px;
    height: 8px;
    background: var(--gold);
  }
  .contact-panel {
    position: absolute;
    left: 0;
    top: 301px;
    width: 1200px;
    height: 372px;
    background: var(--navy);
    color: var(--ink-light);
  }
  .person-name {
    position: absolute;
    left: 121px;
    top: 50px;
    font-size: 58px;
    font-weight: 700;
    line-height: 1;
  }
  .contact-list {
    position: absolute;
    left: 354px;
    top: 158px;
    list-style: none;
    font-size: 40px;
    font-weight: 600;
    line-height: 57px;
  }
</style>
</head>
<body>
  <div class="card">
    <svg class="brand-mark" viewBox="0 0 150 150" aria-hidden="true">
      <circle cx="75" cy="75" r="72" fill="var(--gold)"/>
    </svg>
    <div class="brand-name">MWC</div>
    <div class="brand-rule"></div>

    <div class="gold-band"></div>

    <section class="contact-panel">
      <h1 class="person-name">Liam Carver</h1>
      <ul class="contact-list">
        <li class="contact-phone">Mobile: +61400123456</li>
        <li class="contact-email">liam.carver@meridianworksconsultancy.com.au</li>
        <li class="contact-email">liam.j.carver@mailhub.com</li>
      </ul>
    </section>
  </div>
</body>
</html>
```